Audio Visual company needs WordPress Site re-design

We need a new, simple and sleek redesign of our website, www.vornalisound.com. It is crucial that it is mobile platform friendly! The company emphasis is on commercial sound and video installation.

Examples of what our company does can be found here: http://qelmarview.com/

I am NOT looking for a storefront or an e-commerce site. I would just like an elegant site that describes our services. Perhaps incorporate a sleek showcase into the homepage of projects we have completed. Also would like an elegant menu-bar, perhaps enhance our current site menu or similar.

Here is a link to another site that exhibits the content I am looking for. Their target market is also much like mine.
http://www.haskovelstudio.com/ ........ A polished up version of this site would probably be my ideal site. It has almost EXACTLY the content I am looking for. Exclude the "Printing & signage" category. Needs nicer menus, contact page and project showcase.

Here is another example: http://www.brintolmediaworks.com/ ......... This site has a very nice homepage design with a good layout and feature slider. The site is simple, elegant and to the point.

Target Market(s)

Corporate/commercial business, Educational institutions

Industry/Entity Type

E-Commerce

Font styles to use
Serif
Sans Serif

Requirements
Must have
• Mobile friendly navigation
Nice to have
• HTML5 & CSS3
Should not have
• No Zembric Pulse content. No store templates or e-commerce. We are a service based company not a product sales company

```html
<!DOCTYPE html>
<html lang="en">
<head>
<meta charset="utf-8">
<title>Vornali Sound – Audio &amp; Video Solutions</title>
<link href="https://fonts.googleapis.com/css2?family=Open+Sans:wght@300;400;600;700&family=Roboto+Condensed:wght@300;400;700&display=swap" rel="stylesheet">
<style>
:root{
  --red:#c8161d;
  --red-dark:#9e0f14;
  --ink:#1c1c1c;
  --text:#555;
  --muted:#888;
  --white:#fff;
  --band:#d4d4d4;
  --panel:#e4e4e4;
  --footer:#141414;
}
*{box-sizing:border-box;margin:0;padding:0}
html,body{width:1200px;height:2588px;overflow:hidden}
body{font-family:"Open Sans",Arial,sans-serif;color:var(--text);background:var(--white)}
.wrap{width:1104px;margin:0 auto;position:relative}
h2.section-title{font-family:"Roboto Condensed",Arial,sans-serif;font-weight:300;font-size:46px;color:var(--ink);text-align:center}
h2.section-title span{color:var(--red)}

/* header */
.site-header{height:92px}
.site-header .wrap{height:92px;display:flex;align-items:center;justify-content:space-between}
.brand{display:flex;align-items:center;gap:12px}
.brand-mark{width:34px;height:34px;background:var(--red)}
.brand-name{font-family:"Roboto Condensed",Arial,sans-serif;font-weight:700;font-size:34px;color:var(--ink);line-height:1}
.brand-tag{font-size:12px;color:var(--muted);margin-top:4px;letter-spacing:.5px}
.header-right{display:flex;flex-direction:column;align-items:flex-end;gap:8px}
.header-cta{display:flex;align-items:center;gap:16px;font-size:14px;color:var(--muted)}
.header-cta b{color:var(--red);font-weight:600}
.quote-btn{background:var(--ink);color:var(--white);padding:9px 16px;font-size:14px;font-weight:600}
.social-mini{display:flex;gap:6px}
.social-mini i{width:20px;height:20px;border-radius:50%;background:var(--red);display:block}

/* nav */
.main-nav{height:48px;background:var(--ink)}
.main-nav ul{list-style:none;display:flex;height:48px}
.main-nav li{padding:0 26px;line-height:48px;color:var(--white);font-size:14px;font-weight:600;text-transform:uppercase;letter-spacing:.5px}
.main-nav li.active{background:var(--red)}

/* hero */
.hero{height:580px;position:relative;background:linear-gradient(100deg,#3a3a3a 0%,#7b7b7b 40%,#b9b9b9 70%,#5e5e5e 100%)}
.hero h1{position:absolute;left:0;right:0;top:352px;text-align:center;font-family:"Roboto Condensed",Arial,sans-serif;font-weight:400;font-size:52px;line-height:62px;color:var(--white)}
.hero-arrows{position:absolute;top:520px;left:0;right:0;display:flex;justify-content:center;gap:14px}
.hero-arrows svg{width:40px;height:40px}

/* services */
.services{height:240px;padding-top:20px}
.services .wrap{display:flex;gap:16px}
.service-tile{width:264px;height:220px;position:relative}
.service-tile .pic{height:180px}
.service-tile .label{height:40px;background:var(--red);display:flex;align-items:center;justify-content:space-between;padding:0 12px;color:var(--white);font-size:16px;font-weight:600}
.service-tile .label svg{width:24px;height:24px}

/* welcome */
.welcome{height:380px;padding-top:50px;text-align:center}
.welcome p{width:900px;margin:26px auto 0;font-size:15px;line-height:26px}
.btn-red{display:inline-block;margin-top:34px;background:var(--red);color:var(--white);font-size:13px;font-weight:700;padding:11px 26px;letter-spacing:.5px}

/* gallery */
.gallery{height:440px;background:var(--band);padding-top:46px}
.gallery-body{display:flex;gap:30px;margin-top:30px;align-items:flex-start;padding:0 32px;position:relative}
.gallery-main{width:500px;height:262px;position:relative;background:linear-gradient(160deg,#2a2a2a,#555 60%,#1d1d1d)}
.gallery-main .caption{position:absolute;left:0;bottom:0;width:220px;background:rgba(0,0,0,.75);color:var(--white);padding:10px 14px}
.gallery-main .caption strong{display:block;font-size:16px;font-weight:600}
.gallery-main .caption small{font-size:12px;color:#bbb}
.gallery-thumbs{display:grid;grid-template-columns:repeat(3,164px);gap:10px}
.gallery-thumbs div{height:126px;background:linear-gradient(140deg,#8e1116,#c8161d)}
.gallery-thumbs div.current{outline:4px solid var(--white)}
.gal-arrow{position:absolute;top:118px;width:26px;height:26px}
.gal-arrow.prev{left:0}.gal-arrow.next{right:0}

/* reviews */
.reviews{height:370px;padding-top:44px}
.review-cols{display:flex;gap:60px;margin-top:36px;padding:0 40px}
.review{flex:1}
.review h3{font-family:"Roboto Condensed",Arial,sans-serif;font-weight:400;font-size:24px;color:var(--ink)}
.review .meta{display:flex;align-items:center;gap:10px;margin:6px 0 12px;font-size:12px;color:var(--muted)}
.stars{display:flex;gap:2px}
.stars svg{width:13px;height:13px}
.review p{font-size:13px;line-height:21px}
.view-all{text-align:center;margin-top:34px;font-size:13px;color:var(--red);font-weight:600}

/* contact */
.touch-band{height:100px;background:var(--band);display:flex;align-items:center;justify-content:center}
.contact{height:250px;background:var(--panel);padding-top:36px}
.contact .wrap{display:flex;justify-content:space-between;padding:0 30px}
.contact h4{font-family:"Roboto Condensed",Arial,sans-serif;font-weight:400;font-size:22px;color:var(--ink);margin-bottom:18px}
.contact-col{display:flex;gap:40px;font-size:13px;line-height:22px}
.contact-lines div{display:flex;align-items:center;gap:8px}
.contact-lines svg{width:14px;height:14px}
.follow .circles{display:flex;gap:10px}
.follow .circles i{width:34px;height:34px;border-radius:50%;border:2px solid #555;display:block}
.newsletter p{width:300px;font-size:12px;line-height:19px;margin-bottom:14px}
.newsletter form{display:flex}
.newsletter .field{width:220px;height:32px;background:var(--white);border:1px solid #ccc;font-size:12px;color:#aaa;padding:7px 10px}
.newsletter .submit{height:32px;background:var(--ink);color:var(--white);font-size:12px;padding:8px 14px}

/* footer */
.site-footer{height:88px;background:var(--footer);text-align:center;padding-top:22px}
.site-footer ul{list-style:none;display:flex;justify-content:center;gap:28px;font-size:13px;color:#aaa}
.site-footer ul li:first-child{color:var(--white)}
.site-footer small{display:block;margin-top:10px;font-size:11px;color:#777}
</style>
</head>
<body>

<header class="site-header">
  <div class="wrap">
    <div class="brand">
      <span class="brand-mark"></span>
      <div>
        <div class="brand-name">VORNALI SOUND</div>
        <div class="brand-tag">Sound &amp; Video Solutions</div>
      </div>
    </div>
    <div class="header-right">
      <div class="header-cta">
        <span>Call us for a free Estimate : <b>(555) 014-2207</b></span>
        <span class="quote-btn">Request A Quote</span>
      </div>
      <div class="social-mini"><i></i><i></i><i></i><i></i></div>
    </div>
  </div>
</header>

<nav class="main-nav">
  <div class="wrap">
    <ul>
      <li class="active">Home</li>
      <li>Services</li>
      <li>Contact Us</li>
      <li>Customer Reviews</li>
    </ul>
  </div>
</nav>

<section class="hero" role="img" aria-label="Home theater living room with speakers and a large projection screen">
  <h1>Customizing Audio and Video products for home<br>and business customers since 2007</h1>
  <div class="hero-arrows">
    <svg viewBox="0 0 40 40"><circle cx="20" cy="20" r="19" fill="#222" fill-opacity=".7"/><path d="M23 13l-7 7 7 7" stroke="#fff" stroke-width="2.5" fill="none"/></svg>
    <svg viewBox="0 0 40 40"><circle cx="20" cy="20" r="19" fill="#222" fill-opacity=".7"/><path d="M17 13l7 7-7 7" stroke="#fff" stroke-width="2.5" fill="none"/></svg>
  </div>
</section>

<section class="services">
  <div class="wrap">
    <div class="service-tile">
      <div class="pic" role="img" aria-label="Outdoor digital billboard" style="background:linear-gradient(180deg,#8fb3d6,#d9dee3)"></div>
      <div class="label">Digital Media Signage<svg viewBox="0 0 24 24"><circle cx="12" cy="12" r="11" fill="none" stroke="#fff" stroke-width="2"/><path d="M10 7l5 5-5 5" stroke="#fff" stroke-width="2" fill="none"/></svg></div>
    </div>
    <div class="service-tile">
      <div class="pic" role="img" aria-label="Audio mixing console" style="background:linear-gradient(160deg,#6e5a3c,#b89c6a 50%,#3a3a3a)"></div>
      <div class="label">Live Sound Integration<svg viewBox="0 0 24 24"><circle cx="12" cy="12" r="11" fill="none" stroke="#fff" stroke-width="2"/><path d="M10 7l5 5-5 5" stroke="#fff" stroke-width="2" fill="none"/></svg></div>
    </div>
    <div class="service-tile">
      <div class="pic" role="img" aria-label="Universal remote control" style="background:linear-gradient(160deg,#0f1e3a,#2e4f86 60%,#0b1428)"></div>
      <div class="label">Universal Remotes<svg viewBox="0 0 24 24"><circle cx="12" cy="12" r="11" fill="none" stroke="#fff" stroke-width="2"/><path d="M10 7l5 5-5 5" stroke="#fff" stroke-width="2" fill="none"/></svg></div>
    </div>
    <div class="service-tile">
      <div class="pic" role="img" aria-label="Home theater room with seating" style="background:linear-gradient(160deg,#c9641e,#e79a3c 50%,#6b2c0e)"></div>
      <div class="label">Home Theaters<svg viewBox="0 0 24 24"><circle cx="12" cy="12" r="11" fill="none" stroke="#fff" stroke-width="2"/><path d="M10 7l5 5-5 5" stroke="#fff" stroke-width="2" fill="none"/></svg></div>
    </div>
  </div>
</section>

<section class="welcome">
  <h2 class="section-title">Welcome to <span>Vornali Sound</span></h2>
  <p>Vornali Sound has been customizing audio and video products for home and business customers since 2007. We specialize in the design and installation of residential &amp; commercial sound systems, HD video displays, digital projection &amp; digital signage. We are located in Brenwick Park, a north-west suburb just outside of Halverton. Need an estimate? We will come to you! All of our estimates are done at your home or office for free.</p>
  <span class="btn-red">READ MORE</span>
</section>

<section class="gallery">
  <h2 class="section-title">Installations <span>Gallery</span></h2>
  <div class="wrap gallery-body">
    <svg class="gal-arrow prev" viewBox="0 0 26 26"><circle cx="13" cy="13" r="12" fill="#fff"/><path d="M15 8l-5 5 5 5" stroke="#333" stroke-width="2" fill="none"/></svg>
    <div class="gallery-main" role="img" aria-label="Installed audio equipment rack in a cabinet">
      <div class="caption"><strong>Audio Cabinet</strong><small>Media system installation</small></div>
    </div>
    <div class="gallery-thumbs">
      <div class="current" role="img" aria-label="Equipment rack installation"></div>
      <div role="img" aria-label="Conference room display"></div>
      <div role="img" aria-label="Ceiling speaker install"></div>
      <div role="img" aria-label="Media room setup"></div>
      <div role="img" aria-label="Projector mount"></div>
      <div role="img" aria-label="Theater seating"></div>
    </div>
    <svg class="gal-arrow next" viewBox="0 0 26 26"><circle cx="13" cy="13" r="12" fill="#fff"/><path d="M11 8l5 5-5 5" stroke="#333" stroke-width="2" fill="none"/></svg>
  </div>
</section>

<section class="reviews">
  <h2 class="section-title">Customer <span>Reviews</span></h2>
  <div class="wrap review-cols">
    <article class="review">
      <h3>Lumarq 525 projector</h3>
      <div class="meta"><div class="stars">
        <svg viewBox="0 0 10 10"><path d="M5 0l1.5 3.3 3.5.4-2.6 2.4.7 3.5L5 7.8 1.9 9.6l.7-3.5L0 3.7l3.5-.4z" fill="#c8161d"/></svg><svg viewBox="0 0 10 10"><path d="M5 0l1.5 3.3 3.5.4-2.6 2.4.7 3.5L5 7.8 1.9 9.6l.7-3.5L0 3.7l3.5-.4z" fill="#c8161d"/></svg><svg viewBox="0 0 10 10"><path d="M5 0l1.5 3.3 3.5.4-2.6 2.4.7 3.5L5 7.8 1.9 9.6l.7-3.5L0 3.7l3.5-.4z" fill="#c8161d"/></svg><svg viewBox="0 0 10 10"><path d="M5 0l1.5 3.3 3.5.4-2.6 2.4.7 3.5L5 7.8 1.9 9.6l.7-3.5L0 3.7l3.5-.4z" fill="#c8161d"/></svg><svg viewBox="0 0 10 10"><path d="M5 0l1.5 3.3 3.5.4-2.6 2.4.7 3.5L5 7.8 1.9 9.6l.7-3.5L0 3.7l3.5-.4z" fill="#c8161d"/></svg>
      </div>May 12, 2014 by Anna</div>
      <p>Excellent and detailed professional, with installation of interactive projector, as well as mounting it on the wall board. Highly recommend Andrew.</p>
    </article>
    <article class="review">
      <h3>Lumarq 525 projector</h3>
      <div class="meta"><div class="stars">
        <svg viewBox="0 0 10 10"><path d="M5 0l1.5 3.3 3.5.4-2.6 2.4.7 3.5L5 7.8 1.9 9.6l.7-3.5L0 3.7l3.5-.4z" fill="#c8161d"/></svg><svg viewBox="0 0 10 10"><path d="M5 0l1.5 3.3 3.5.4-2.6 2.4.7 3.5L5 7.8 1.9 9.6l.7-3.5L0 3.7l3.5-.4z" fill="#c8161d"/></svg><svg viewBox="0 0 10 10"><path d="M5 0l1.5 3.3 3.5.4-2.6 2.4.7 3.5L5 7.8 1.9 9.6l.7-3.5L0 3.7l3.5-.4z" fill="#c8161d"/></svg><svg viewBox="0 0 10 10"><path d="M5 0l1.5 3.3 3.5.4-2.6 2.4.7 3.5L5 7.8 1.9 9.6l.7-3.5L0 3.7l3.5-.4z" fill="#c8161d"/></svg><svg viewBox="0 0 10 10"><path d="M5 0l1.5 3.3 3.5.4-2.6 2.4.7 3.5L5 7.8 1.9 9.6l.7-3.5L0 3.7l3.5-.4z" fill="#c8161d"/></svg>
      </div>May 12, 2014 by Mark</div>
      <p>Excellent and detailed professional, with installation of interactive projector, as well as mounting it on the wall board. Highly recommend Andrew.</p>
    </article>
    <article class="review">
      <h3>Lumarq 525 projector</h3>
      <div class="meta"><div class="stars">
        <svg viewBox="0 0 10 10"><path d="M5 0l1.5 3.3 3.5.4-2.6 2.4.7 3.5L5 7.8 1.9 9.6l.7-3.5L0 3.7l3.5-.4z" fill="#c8161d"/></svg><svg viewBox="0 0 10 10"><path d="M5 0l1.5 3.3 3.5.4-2.6 2.4.7 3.5L5 7.8 1.9 9.6l.7-3.5L0 3.7l3.5-.4z" fill="#c8161d"/></svg><svg viewBox="0 0 10 10"><path d="M5 0l1.5 3.3 3.5.4-2.6 2.4.7 3.5L5 7.8 1.9 9.6l.7-3.5L0 3.7l3.5-.4z" fill="#c8161d"/></svg><svg viewBox="0 0 10 10"><path d="M5 0l1.5 3.3 3.5.4-2.6 2.4.7 3.5L5 7.8 1.9 9.6l.7-3.5L0 3.7l3.5-.4z" fill="#c8161d"/></svg><svg viewBox="0 0 10 10"><path d="M5 0l1.5 3.3 3.5.4-2.6 2.4.7 3.5L5 7.8 1.9 9.6l.7-3.5L0 3.7l3.5-.4z" fill="#c8161d"/></svg>
      </div>May 12, 2014 by Lisa</div>
      <p>Excellent and detailed professional, with installation of interactive projector, as well as mounting it on the wall board. Highly recommend Andrew.</p>
    </article>
  </div>
  <div class="view-all">View All Reviews</div>
</section>

<div class="touch-band"><h2 class="section-title">Get In <span>Touch</span></h2></div>

<section class="contact">
  <div class="wrap">
    <div>
      <h4>Contact</h4>
      <div class="contact-col">
        <p>Lorem ipsum dolor sit amet,<br>consectetur adipiscing elit,<br>sed do eiusmod tempor<br>incididunt</p>
        <div class="contact-lines">
          <div><svg viewBox="0 0 14 14"><path d="M3 1l2 3-1.5 1.5a8 8 0 0 0 5 5L10 9l3 2-1 2.5C6 13 1 8 .5 2z" fill="#555"/></svg>(555) 014-2207</div>
          <div><svg viewBox="0 0 14 14"><path d="M3 1l2 3-1.5 1.5a8 8 0 0 0 5 5L10 9l3 2-1 2.5C6 13 1 8 .5 2z" fill="#555"/></svg>(555) 014-2208</div>
          <div><svg viewBox="0 0 14 14"><rect x="1" y="3" width="12" height="8" fill="none" stroke="#555" stroke-width="1.5"/><path d="M1 3l6 5 6-5" stroke="#555" stroke-width="1.5" fill="none"/></svg>info@vornalisound.com</div>
        </div>
      </div>
    </div>
    <div class="follow">
      <h4>Follow Us On</h4>
      <div class="circles"><i></i><i></i><i></i><i></i></div>
    </div>
    <div class="newsletter">
      <h4>Newsletter Sign Up</h4>
      <p>Sign up to receive project news, service updates and seasonal offers straight to your inbox.</p>
      <form><span class="field">Enter your Email ID</span><span class="submit">Subscribe</span></form>
    </div>
  </div>
</section>

<footer class="site-footer">
  <ul>
    <li>Home</li><li>Services</li><li>Contact</li><li>Customer Reviews</li><li>Support</li><li>Terms &amp; Conditions</li><li>Privacy Policy</li>
  </ul>
  <small>All rights reserved. Copyright 2014</small>
</footer>

</body>
</html>
```